Business Card Design

We do Metal Roofing, fascia and gutter and edge protection [safety rail].

Industry/Entity Type

Business

Contact Information for Business Card

Tarnwell Roof Plumbing. Metal Roofing, Fascia and Gutter, Edge Protection
Colin 0468305172
Finn 0419587364
tr7win5@mailvane.com
Lic: 614903K
ABN:52716340951

```html
<!DOCTYPE html>
<html lang="en">
<head>
<meta charset="utf-8">
<title>Tarnwell Roof Plumbing – Business Card</title>
<link rel="stylesheet" href="https://fonts.googleapis.com/css2?family=Open+Sans:wght@400;600;700&display=swap">
<style>
  :root {
    --brand-red: #ec1c2a;
    --ink: #333333;
    --card-white: #ffffff;
    --backdrop: #1a1a1a;
  }
  * { margin: 0; padding: 0; box-sizing: border-box; }
  html, body {
    width: 1200px;
    height: 900px;
    overflow: hidden;
    background: var(--backdrop);
    font-family: "Open Sans", Arial, sans-serif;
  }
  .canvas {
    position: relative;
    width: 1200px;
    height: 900px;
  }
  .card {
    position: absolute;
    top: 170px;
    width: 347px;
    height: 561px;
    overflow: hidden;
  }
  .card--front {
    left: 259px;
    background: var(--card-white);
    color: var(--ink);
    text-align: center;
  }
  .card--back {
    left: 631px;
    background: var(--brand-red);
    color: var(--card-white);
    text-align: center;
  }
  .tab {
    position: absolute;
    left: 102px;
    width: 143px;
    background: var(--brand-red);
  }
  .tab--top { top: 0; height: 30px; }
  .tab--bottom { bottom: 0; height: 28px; }

  .wordmark {
    position: absolute;
    left: 0;
    width: 100%;
    font-weight: 400;
    line-height: 1;
    letter-spacing: 1px;
  }
  .card--front .wordmark {
    top: 118px;
    font-size: 62px;
    color: var(--brand-red);
  }
  .trade-name {
    position: absolute;
    top: 218px;
    left: 0;
    width: 100%;
    font-size: 33px;
    font-weight: 700;
    line-height: 1;
    color: var(--ink);
  }
  .contacts {
    position: absolute;
    top: 296px;
    left: 0;
    width: 100%;
    font-size: 14.5px;
    line-height: 1.4;
  }
  .contact__name {
    color: var(--brand-red);
    font-weight: 700;
    font-size: 18px;
    line-height: 1.2;
  }
  .contact__phone { margin-bottom: 9px; }
  .email {
    display: flex;
    justify-content: center;
    align-items: center;
    gap: 12px;
    margin: 2px 0 9px;
    padding-right: 16px;
  }
  .email svg { width: 11px; height: 8px; }
  .registration { line-height: 1.45; }

  .card--back .wordmark {
    top: 358px;
    font-size: 72px;
    color: var(--card-white);
  }
  .services {
    position: absolute;
    top: 482px;
    left: 0;
    width: 100%;
    font-size: 14.5px;
    line-height: 1.42;
  }
</style>
</head>
<body>
<main class="canvas">
  <section class="card card--front" aria-label="Card front">
    <div class="tab tab--top"></div>
    <div class="wordmark">Tarnwell</div>
    <div class="trade-name">Roof Plumbing</div>
    <div class="contacts">
      <div class="contact__name">Colin</div>
      <div class="contact__phone">0468305172</div>
      <div class="contact__name">Finn</div>
      <div class="contact__phone">0419587364</div>
      <div class="email">
        <svg viewBox="0 0 11 8" aria-hidden="true">
          <rect x="0" y="0" width="11" height="8" fill="#ec1c2a"/>
          <polyline points="0.5,0.8 5.5,4.8 10.5,0.8" fill="none" stroke="#ffffff" stroke-width="1"/>
        </svg>
        <span>tr7win5@mailvane.com</span>
      </div>
      <div class="registration">
        <div>Lic: 614903K</div>
        <div>ABN:52716340951</div>
      </div>
    </div>
    <div class="tab tab--bottom"></div>
  </section>

  <section class="card card--back" aria-label="Card back">
    <div class="wordmark">Tarnwell</div>
    <div class="services">
      <div>Metal Roofing, Fascia and Gutter</div>
      <div>Edge Protection</div>
    </div>
  </section>
</main>
</body>
</html>
```